Hunting club needs a new web design !

We need a new web design for our hunting club located in Poland, called "ZAWIRA". The club was founded in 1945. Colors that we would like to see in the project are the colors of the forest. The website should be built in such a way that all text elements can be changed to another language and can't be graphic.
"ZAWIRA" means - big, thick forest in which the game, small and big resides

Target Market(s)

hunters,

Industry/Entity Type

Hunting

Coding

Coded - Design and coding required

Number of Pages Required

5+ page

Font styles to use
Decorative

Colors

Designer to choose colors to be used in the design.

Requirements
Must have
• current date, calendar,
• must contain almost all materials from our current web page
• http://zawira-dolnomokra.webnika.pl/
• new web address: zawiradmk.pl
Nice to have
• current weather in three hunting regions that we allowed to hunt, or indicated by the visitor on the map placed on our web,
• actual phase of the moon, actual moon rising hour, actual moon set hour, actual sun rise hour, actual sun set hour, current weather in region (stalowa wola, poland)
• wood, forest, deers, boars,
Should not have
• mountain photos, modern look, white or bright backgrounds,

```html
<!DOCTYPE html>
<html lang="pl">
<head>
<meta charset="utf-8">
<title>Koło Łowieckie Zawira w Dolnej Mokrej</title>
<link href="https://fonts.googleapis.com/css2?family=Crimson+Text:wght@400;600&family=Roboto:wght@400;500;700&display=swap" rel="stylesheet">
<style>
:root{
  --cream:#f6ecd9;
  --cream-dark:#e9d8b8;
  --forest:#2e7b2c;
  --bark:#3a2616;
  --bark-dark:#24170d;
  --bark-mid:#4e3520;
  --panel:#3b2a1c;
  --panel-edge:#6a4c30;
  --field:#ecd3b0;
  --copper:#b5683a;
  --copper-dark:#8f4e27;
  --text-light:#f3e8d6;
  --text-muted:#cdbba2;
  --ink:#3a2a1a;
}
*{box-sizing:border-box;margin:0;padding:0}
html,body{width:1200px;height:2848px;overflow:hidden;background:var(--bark-dark)}
body{position:relative;font-family:"Roboto",sans-serif;color:var(--text-light)}

/* Header */
.site-header{position:absolute;left:0;top:0;width:1200px;height:140px;background:linear-gradient(#fbf5e9,var(--cream-dark))}
.brand-name{position:absolute;left:76px;top:26px;font-family:"Crimson Text",serif;font-weight:600;font-size:54px;line-height:1;color:var(--forest);letter-spacing:1px}
.brand-mark{position:absolute;left:320px;top:26px;width:54px;height:54px;border:2px solid var(--bark-mid);border-radius:50%}
.club-title{position:absolute;left:404px;top:28px;width:300px;text-align:center;font-family:"Crimson Text",serif;color:var(--forest);line-height:1}
.club-title .line1{font-size:29px}
.club-title .line2{font-size:21px;margin-top:4px}
.tagline{position:absolute;left:70px;top:104px;width:640px;text-align:center;font-size:12.5px;color:var(--ink)}
.lang{position:absolute;right:40px;top:8px;display:flex;gap:12px;font-size:10px;color:var(--ink)}
.lang span{display:flex;align-items:center;gap:4px}
.lang i{display:block;width:14px;height:9px;border:1px solid #999}
.astro{position:absolute;left:730px;top:22px;width:398px}
.astro-title{display:flex;align-items:center;gap:8px;padding-left:12px;font-size:15px;color:var(--ink);font-weight:500}
.astro-box{margin-top:10px;display:flex;height:68px;border:2px solid var(--copper-dark);border-radius:8px;overflow:hidden}
.astro-country{flex:1;background:var(--cream);display:flex;align-items:center;justify-content:center;font-size:17px;color:var(--copper-dark);gap:8px}
.astro-moon{width:180px;background:var(--copper-dark);display:flex;align-items:center;gap:10px;padding-left:14px}
.moon-disc{width:42px;height:42px;border-radius:50%;background:#2a2a2a;border:2px solid #c9c2b4}
.moon-text b{display:block;font-size:20px;color:#fff}
.moon-text span{font-size:13px;color:var(--cream)}

/* Navigation */
.main-nav{position:absolute;left:0;top:140px;width:1200px;height:42px;background:linear-gradient(#4a3020,#2b1b10);display:flex;justify-content:center}
.main-nav a{color:#fff;text-decoration:none;font-size:16px;font-weight:500;padding:0 19px;line-height:42px;border-right:1px solid #6b4a30}
.main-nav a:last-child{border-right:0}

/* Hero */
.hero{position:absolute;left:0;top:182px;width:1200px;height:563px;
  background:
    linear-gradient(180deg,rgba(40,45,30,.55) 0%,rgba(40,45,30,0) 35%,rgba(0,0,0,0) 60%,rgba(150,150,60,.55) 85%,rgba(120,130,50,.7) 100%),
    radial-gradient(ellipse 420px 300px at 300px 300px,rgba(140,60,40,.45),rgba(140,60,40,0) 70%),
    radial-gradient(ellipse 260px 420px at 930px 280px,rgba(70,55,40,.55),rgba(70,55,40,0) 75%),
    linear-gradient(100deg,#5e6a48 0%,#8a8a5a 30%,#9c8c62 50%,#8a6a3a 72%,#b0682c 100%)}

/* Welcome */
.welcome{position:absolute;left:0;top:745px;width:1200px;height:530px;background:linear-gradient(90deg,#2b1a0f,#47301d 20%,#3a2616 45%,#4c331f 70%,#2b1a0f);text-align:center}
.welcome .pre{margin-top:76px;font-family:"Crimson Text",serif;font-size:30px}
.welcome h1{font-family:"Crimson Text",serif;font-weight:400;font-size:44px;line-height:1.1}
.divider{width:60px;height:1px;background:var(--text-muted);margin:14px auto 24px}
.welcome p{width:700px;margin:0 auto 16px;font-size:14.5px;line-height:26px;color:var(--text-light)}
.btn{display:inline-block;background:var(--copper);color:#fff;font-size:13px;font-weight:700;text-transform:uppercase;border-radius:5px;padding:8px 18px}
.welcome .btn{margin-top:10px}

/* Forest band */
.forest{position:absolute;left:0;top:1275px;width:1200px;height:1205px;background:linear-gradient(#7a6a3e 0%,#8b7a55 18%,#6d5333 45%,#4a3524 70%,#5b4a3a 85%,#3a2a1e 100%)}
.panel{position:absolute;background:rgba(46,31,20,.93);border:2px solid var(--panel-edge);border-radius:6px}
.panel h2{font-family:"Crimson Text",serif;font-weight:400;font-size:28px;text-align:center;margin-top:8px}
.panel .divider{margin:6px auto 14px}
.field{background:var(--field);border-radius:3px;height:36px;margin:0 16px 10px;color:var(--ink);font-size:13px;padding:10px 12px}
.field.tall{height:98px}
.panel .btn.full{display:block;margin:14px 16px 0;text-align:center;padding:11px}
.quote{padding:0 30px;text-align:center;font-size:14px;line-height:25px}
.quote-author{text-align:center;font-size:15px;font-weight:700;margin-top:12px}
.moon-form label{display:block;margin:6px 16px 4px;font-size:13px}
.select{display:flex;justify-content:space-between;align-items:center}
.select:after{content:"";border:7px solid transparent;border-top:8px solid var(--ink);margin-top:7px}

.block-title{font-family:"Crimson Text",serif;font-size:30px;padding:6px 12px}
.gal-item{display:flex;margin:0 14px 10px;height:84px;background:var(--bark-mid)}
.thumb{width:134px;height:84px;flex:none}
.gal-item div.txt{padding:12px 10px;font-size:13px;white-space:nowrap}
.gal-item b{display:block;font-size:15px;margin-bottom:6px}
.monografia{position:absolute;left:432px;top:1833px;width:336px;height:419px;background:linear-gradient(160deg,#4f7a3a,#3f5d2a 50%,#6b5a3a);border:2px solid var(--panel-edge);overflow:hidden}
.mono-head{display:flex;align-items:center;gap:10px;padding:20px 14px 10px}
.mono-head i{width:44px;height:44px;border:2px solid var(--text-light);border-radius:50%}
.mono-head span{font-family:"Crimson Text",serif;font-size:26px;font-weight:600;color:var(--field);letter-spacing:1px}
.mono-list{position:absolute;left:12px;top:96px;width:200px;background:rgba(25,40,20,.55);padding:8px 10px;list-style:none}
.mono-list li{font-size:13px;line-height:25.5px;white-space:nowrap;color:#fff}
.mono-list li:before{content:"■ ";font-size:8px;vertical-align:middle}
.mono-years{position:absolute;right:16px;bottom:10px;font-size:20px;font-family:"Crimson Text",serif;color:var(--field)}
.news-item{display:flex;gap:10px;margin:0 12px 20px;height:60px}
.news-item .thumb{width:88px;height:60px}
.news-item div.txt{font-size:13px;line-height:17px}
.news-item small{font-size:12px;display:block}
.band-photo{position:absolute;left:0;top:2252px;width:1200px;height:228px;background:linear-gradient(#8a8272,#6f6653 60%,#4a3a2a)}

/* Footer */
.site-footer{position:absolute;left:0;top:2480px;width:1200px;height:368px;background:linear-gradient(90deg,#1f140c,#33221a 30%,#271910 60%,#1f140c)}
.foot-mark{position:absolute;left:250px;top:40px;width:700px;display:flex;align-items:center;gap:16px}
.foot-mark hr{flex:1;border:0;border-top:1px solid #7a6a5a}
.foot-mark span{font-family:"Crimson Text",serif;font-size:28px;font-weight:600;color:var(--text-light)}
.foot-col{position:absolute;top:112px;font-size:13px;line-height:26px;color:var(--text-muted)}
.foot-col h3{font-size:15px;font-weight:700;color:#fff;margin-bottom:10px}
.two{display:flex;gap:70px}
.social div{display:flex;align-items:center;gap:10px;line-height:35px}
.social i{width:26px;height:26px;border-radius:50%;background:var(--text-light)}
.subscribe{display:flex;margin-top:16px}
.subscribe span{width:236px;height:36px;background:var(--field);color:#7a6650;font-size:12px;padding:10px 12px}
.subscribe b{background:var(--copper);color:#fff;font-size:13px;padding:10px 14px}
.copyright{position:absolute;left:0;bottom:0;width:1200px;border-top:1px solid #4a3a2a;text-align:center;font-size:12.5px;color:var(--text-muted);padding:14px 0}
</style>
</head>
<body>

<header class="site-header">
  <div class="brand-name">ZAWIRA</div>
  <div class="brand-mark"></div>
  <div class="club-title"><div class="line1">Koło Łowieckie Zawira</div><div class="line2">w Dolnej Mokrej</div></div>
  <div class="tagline">Uhonorowane Odznaką Zasługi Łowieckiej "ZŁOM", oraz Medalem Świętego Huberta</div>
  <div class="lang"><span><i style="background:linear-gradient(#fff 50%,#d4213d 50%)"></i>PL</span><span><i style="background:#2a3f8a"></i>EN</span><span><i style="background:linear-gradient(#111 33%,#d00 33% 66%,#fc0 66%)"></i>DE</span></div>
  <div class="astro">
    <div class="astro-title">
      <svg width="34" height="26" viewBox="0 0 34 26" aria-hidden="true"><circle cx="12" cy="12" r="6" fill="none" stroke="#8a6a3a" stroke-width="2"/><path d="M8 22h20a5 5 0 0 0-4-8 7 7 0 0 0-13 2 3 3 0 0 0-3 6z" fill="#fbf5e9" stroke="#8a6a3a" stroke-width="2"/></svg>
      Sunrise, Sunset, and Moon Times for Today
    </div>
    <div class="astro-box">
      <div class="astro-country">Poland <svg width="12" height="8" viewBox="0 0 12 8" aria-hidden="true"><path d="M0 0h12L6 8z" fill="#8f4e27"/></svg></div>
      <div class="astro-moon"><div class="moon-disc"></div><div class="moon-text"><b>Moon: 7.9%</b><span>Waning Crescent</span></div></div>
    </div>
  </div>
</header>

<nav class="main-nav">
  <a>Home</a><a>About Us</a><a>Hunting Areas</a><a>Hunting Offer</a><a>Hunting Season</a><a>Weather</a><a>News</a><a>Gallery</a><a>Contact</a>
</nav>

<div class="hero" role="img" aria-label="Roaring red deer stag in a meadow beside a wooden hunting stand at the forest edge in autumn"></div>

<section class="welcome">
  <div class="pre">Welcome to</div>
  <h1>Koło Łowieckie Zawira w Dolnej Mokrej</h1>
  <div class="divider"></div>
  <p>Witamy na stronie internetowej Koła ZAWIRA w Dolnej Mokrej. Mamy nadzieję, że przekazywane wiadomości ułatwią wszystkim myśliwym, oraz sympatykom łowiectwa poznanie zakresu działania i problemów naszego Koła. Początki mogą być trudne, sądzimy jednak, że z biegiem czasu uda nam się rozbudować stronę o inne interesujące tematy z naszej działalności.</p>
  <p>Kolegów myśliwych KŁ. ZAWIRA prosimy o zaglądanie do zakładki NOWOŚCI,</p>
  <p>w której zamieszczane będą bieżące informacje oraz komunikaty.</p>
  <span class="btn">Read more</span>
</section>

<section class="forest" role="img" aria-label="Misty autumn forest with a hunting stand and a deer in the clearing"></section>

<div class="panel" style="left:76px;top:1443px;width:329px;height:342px">
  <h2>Quick Question</h2><div class="divider"></div>
  <div class="field">Name</div>
  <div class="field">Email</div>
  <div class="field tall">Message</div>
  <span class="btn full">Submit</span>
</div>

<div class="panel" style="left:435px;top:1443px;width:330px;height:342px">
  <h2>Testimonial</h2><div class="divider"></div>
  <p class="quote">"Lorem ipsum dolor sit amet, consectetur adipiscing elit, sed do eiusmod tempor incididunt ut labore et dolore magna aliqua. Ut enim ad minim veniam, quis nostrud exercitation ullamco laboris nisi ut aliquip ex ea commodo consequat. Duis aute irure dolor in reprehenderit in voluptate velit esse cillum dolore eu fugiat nulla pariatur."</p>
  <div class="quote-author">-Tomasz Wrzos</div>
</div>

<div class="panel moon-form" style="left:795px;top:1443px;width:329px;height:342px">
  <h2>Fazy Księżyca</h2><div class="divider"></div>
  <label>Rok</label><div class="field select">2017</div>
  <label>Miesiąc:</label><div class="field select">Lipiec</div>
  <label>Dzień:</label><div class="field select">5</div>
  <span class="btn full">Pokaż fazy księżyca</span>
</div>

<div class="panel" style="left:76px;top:1833px;width:1048px;height:419px;border-radius:6px"></div>

<div style="position:absolute;left:78px;top:1835px;width:352px">
  <div class="block-title">Galeria</div>
  <div class="gal-item"><div class="thumb" role="img" aria-label="Hunters gathered in a field" style="background:linear-gradient(#6f8a4a,#4a5a2e)"></div><div class="txt"><b>ROK 2015</b>Rozpoczęcie sezonu</div></div>
  <div class="gal-item"><div class="thumb" role="img" aria-label="Group of hunters at the Saint Hubert hunt" style="background:linear-gradient(#7a7a5a,#4a4a30)"></div><div class="txt"><b>ROK 2014</b>Polowanie - Święty Hubert</div></div>
  <div class="gal-item"><div class="thumb" role="img" aria-label="Hunters closing the season in the woods" style="background:linear-gradient(#5a6a4a,#3a3a2a)"></div><div class="txt"><b>ROK 2013</b>Zakończenie sezonu</div></div>
  <span class="btn" style="margin-left:14px">More</span>
</div>

<div class="monografia" role="img" aria-label="Wooden roadside shrine in the forest">
  <div class="mono-head"><i></i><span>MONOGRAFIA</span></div>
  <ul class="mono-list">
    <li>Historia powstania</li><li>Gospodarka łowiecka</li><li>Polowania komercyjne</li><li>Polowania hubertowskie</li><li>Kult Św.Huberta</li><li>Sztandar</li><li>Strzelectwo</li><li>Konkursy przyrodnicze</li><li>Strzelectwo</li><li>Kynologia</li>
  </ul>
  <div class="mono-years">1945 - 2015</div>
</div>

<div style="position:absolute;left:770px;top:1835px;width:352px">
  <div class="block-title">News</div>
  <div class="news-item"><div class="thumb" role="img" aria-label="Autumn leaves" style="background:linear-gradient(#c8702a,#7a3a1a)"></div><div class="txt"><small>20.07.2017</small>Lorem ipsum dolor sit amet, consectetur adipiscing elit</div></div>
  <div class="news-item"><div class="thumb" role="img" aria-label="Hunting stand by a lake" style="background:linear-gradient(#8aa0b0,#5a6a4a)"></div><div class="txt"><small>23.07.2017</small>Lorem ipsum dolor sit amet, consectetur adipiscing elit</div></div>
  <div class="news-item"><div class="thumb" role="img" aria-label="Forest at sunset" style="background:linear-gradient(#e0a050,#5a4a6a)"></div><div class="txt"><small>24.07.2017</small>Lorem ipsum dolor sit amet, consectetur adipiscing elit</div></div>
  <div class="news-item"><div class="thumb" role="img" aria-label="Deer in a meadow" style="background:linear-gradient(#7a8a4a,#8a5a30)"></div><div class="txt"><small>25.07.2017</small>Lorem ipsum dolor sit amet, consectetur adipiscing elit</div></div>
  <span class="btn" style="margin-left:12px">More</span>
</div>

<div class="band-photo" role="img" aria-label="Hunters with rifles in a misty forest"></div>

<footer class="site-footer">
  <div class="foot-mark"><hr><span>ZAWIRA</span><hr></div>
  <div class="foot-col" style="left:72px">
    <h3>Quick Links</h3>
    <div class="two"><div>Home<br>About Us<br>Hunting Areas<br>Hunting Offer<br>Hunting Season</div><div>Weather<br>News<br>Gallery<br>Contact</div></div>
  </div>
  <div class="foot-col" style="left:332px">
    <h3>Contact Us</h3>
    Lorem ipsum dolor sit.<br>Street Name, 000000<br>City Name<br><div style="height:10px"></div>P: 100-000-0000<br>E: info@zawiradmk.pl
  </div>
  <div class="foot-col social" style="left:578px">
    <h3>Keep in Touch</h3>
    <div><i></i>Leśny Krąg</div><div><i></i>Ptasi Głos</div><div><i></i>Kadr Lasu</div><div><i></i>Sieć Myśliwych</div>
  </div>
  <div class="foot-col" style="left:792px;width:340px">
    <h3>Get The Subscribe Newsletter</h3>
    Lorem ipsum dolor sit amet, consectetur adipi scing elit, sed do eiusmod tempor incididunt.
    <div class="subscribe"><span>Enter your email address</span><b>Subscribe</b></div>
  </div>
  <div class="copyright">© 2017 Koło Łowieckie Zawira w Dolnej Mokrej. All Rights Reserved.</div>
</footer>

</body>
</html>
```